Group Medical Practice needs stationery, business cards etc. designed

We need stationery designed for a multisite practice that offers primary medical, dental and behavioral healthcare. We would like a design that is consistent for letterhead, business cards, Microsoft Outlook stationery etc. We have attached our new logo design.

Business

```html
<!DOCTYPE html>
<html lang="en">
<head>
<meta charset="utf-8">
<title>Cedar Ridge Health Services – Stationery</title>
<link href="https://fonts.googleapis.com/css2?family=Fira+Sans:wght@400;500;600&display=swap" rel="stylesheet">
<style>
  :root {
    --backdrop: #5c5c5e;
    --paper: #ffffff;
    --brand-blue: #1a6fb8;
    --brand-green: #8cc63f;
    --ink: #6d6e70;
    --ink-dark: #58595b;
    --rule: #1a6fb8;
  }
  * { margin: 0; padding: 0; box-sizing: border-box; }
  html, body { width: 1000px; height: 1200px; overflow: hidden; }
  body {
    position: relative;
    background: var(--backdrop);
    font-family: "Fira Sans", Arial, sans-serif;
    color: var(--ink);
  }

  /* Letterhead */
  .letterhead {
    position: absolute; left: 127px; top: 65px;
    width: 595px; height: 842px;
    background: var(--paper);
  }
  .brand {
    position: absolute;
    display: flex; align-items: center; gap: 10px;
  }
  .brand-dot {
    flex: none; border-radius: 50%;
    background: var(--brand-green);
  }
  .brand-name {
    color: var(--brand-blue); font-weight: 600; line-height: 1.1;
  }
  .brand-name span { display: block; }

  .letterhead .brand { left: 41px; top: 44px; }
  .letterhead .brand-dot { width: 22px; height: 22px; }
  .letterhead .brand-name { font-size: 19px; }
  .letterhead .brand-name span + span { font-size: 11px; letter-spacing: 0.6px; }

  .letter-body {
    position: absolute; left: 99px; top: 182px; width: 440px;
    font-size: 11.6px; line-height: 14.5px; color: var(--ink);
    white-space: nowrap;
  }
  .letter-salutation { font-weight: 600; color: var(--ink-dark); margin-bottom: 14.5px; }
  .letter-body p + p { margin-top: 14.5px; }

  .signature {
    position: absolute; right: 82px; top: 604px; text-align: center;
  }
  .signature-name { font-size: 16px; color: var(--brand-blue); line-height: 1.2; }
  .signature-title { font-size: 10px; color: var(--ink); }

  .letter-footer {
    position: absolute; left: 0; top: 775px; width: 100%; height: 44px;
    font-size: 8.5px; line-height: 11px; color: var(--ink);
  }
  .footer-address { position: absolute; right: 419px; top: 7px; text-align: center; }
  .footer-phone { position: absolute; left: 264px; top: 10px; }
  .footer-web { position: absolute; left: 439px; top: 10px; }
  .footer-rule {
    position: absolute; top: 0; width: 2px; height: 44px; background: var(--rule);
  }
  .label { font-weight: 600; color: var(--ink-dark); }

  /* Business cards */
  .card {
    position: absolute; width: 255px; height: 141px; background: var(--paper);
  }
  .card-front { left: 308px; top: 979px; }
  .card-front .brand { left: 0; right: 0; top: 50px; justify-content: center; }
  .card-front .brand-dot { width: 20px; height: 20px; }
  .card-front .brand-name { font-size: 18px; }
  .card-front .brand-name span + span { font-size: 10px; letter-spacing: 0.5px; }

  .card-back { left: 617px; top: 978px; }
  .card-back .brand { left: 22px; top: 16px; gap: 5px; }
  .card-back .brand-dot { width: 9px; height: 9px; }
  .card-back .brand-name { font-size: 8.5px; }
  .card-back .brand-name span + span { font-size: 5.5px; letter-spacing: 0.3px; }
  .card-person { position: absolute; right: 22px; top: 63px; text-align: right; }
  .card-person .signature-name { font-size: 15px; }
  .card-person .signature-title { font-size: 9px; }
  .card-contacts { font-size: 6px; line-height: 8px; color: var(--ink); }
  .card-rule { position: absolute; top: 106px; width: 2px; height: 25px; background: var(--rule); }
  .card-address { position: absolute; left: 27px; top: 109px; text-align: center; }
  .card-phone { position: absolute; left: 150px; top: 109px; }
</style>
</head>
<body>

<section class="letterhead">
  <div class="brand">
    <span class="brand-dot"></span>
    <div class="brand-name"><span>Cedar Ridge</span><span>Health Services</span></div>
  </div>

  <div class="letter-body">
    <p class="letter-salutation">Lorem ipsum,</p>
    <p>Mauris at vestibulum elit. Mauris sed malesuada turpis, nec lobortis mi. Proin<br>nec lacus condimentum, mattis dolor nec, luctus enim. Nunc in nunc metus.<br>Donec convallis diam mauris, quis eleifend odio tincidunt sed. Proin sed nulla<br>aliquet, tincidunt est sit amet, eleifend ipsum.</p>
    <p>Aenean vitae maximus metus, at hendrerit enim. Donec cursus ante sed euis-<br>mod tempus. Nam quis tortor varius, pellentesque tortor ac, porta mi. Integer<br>lorem sem, mollis ac pulvinar ac, rutrum vitae massa. Nam ut mauris id tellus<br>aliquam commodo. Proin iaculis turpis ut arcu ullamcorper, vel commodo mauris<br>feugiat. Etiam finibus in nisl sit amet ultrices.</p>
    <p>Pellentesque non efficitur nibh. In sollicitudin accumsan velit. Cras mollis erat<br>lectus, et ultrices felis vehicula sed. Proin odio libero, consectetur non felis quis,<br>scelerisque fringilla urna. Cras venenatis rhoncus enim, id finibus nibh maximus<br>ut. Morbi scelerisque laoreet tempor. Phasellus dignissim lectus at lacus inter-<br>dum pulvinar. Ut pulvinar imperdiet massa, ac molestie magna cursus non. Duis<br>diam erat, finibus ac venenatis nec, gravida vel arcu. Pellentesque non rutrum<br>nibh. Aenean tristique metus et libero ornare pretium. Nullam fermentum mollis<br>vulputate.</p>
  </div>

  <div class="signature">
    <div class="signature-name">Warren Tillbury</div>
    <div class="signature-title">President and C.E.O</div>
  </div>

  <footer class="letter-footer">
    <div class="footer-address"><span class="label">Cedar Ridge,</span> Health service<br>42 Alder Lane Ste 210,<br>Millbrook Falls, Virginia 24190</div>
    <span class="footer-rule" style="left:221px"></span>
    <div class="footer-phone"><span class="label">Phone</span>&nbsp; 00321 654 987<br>&nbsp;&nbsp;<span class="label">Fax</span>&nbsp;&nbsp; 00 321 654 98</div>
    <span class="footer-rule" style="left:398px"></span>
    <div class="footer-web"><span class="label">www.CedarRidgeHealth.com</span><br>info@cedarridgehealth.com</div>
  </footer>
</section>

<section class="card card-front">
  <div class="brand">
    <span class="brand-dot"></span>
    <div class="brand-name"><span>Cedar Ridge</span><span>Health Services</span></div>
  </div>
</section>

<section class="card card-back">
  <div class="brand">
    <span class="brand-dot"></span>
    <div class="brand-name"><span>Cedar Ridge</span><span>Health Services</span></div>
  </div>
  <div class="card-person">
    <div class="signature-name">Warren Tillbury</div>
    <div class="signature-title">President and C.E.O</div>
  </div>
  <span class="card-rule" style="left:16px"></span>
  <div class="card-contacts card-address">42 Alder Lane Ste 210<br>Millbrook Falls, Virginia 24190</div>
  <span class="card-rule" style="left:134px"></span>
  <div class="card-contacts card-phone"><span class="label">Phone</span> 00321 654 987<br>&nbsp;&nbsp;<span class="label">Fax</span>&nbsp; 00 321 654 98</div>
  <span class="card-rule" style="left:236px"></span>
</section>

</body>
</html>
```